Bref créative
Website template for salsa company
Abuela Rufina's Roasted Dip
Food
www.RoastedDipco.com
Startup salsa company. We aim to change peoples thinking that salsa is just for "Chips & Salsa". The website will contain recipes and ideas for using the salsa in others ways as well as an ecommerce page where you can buy it.
Dislike dark backgrounds
Like easy navigation
Like dynamic content
Like a little humor in pictures such characters (peppers that smile etc)
Colorful
Humorous
top
www.kendrawpepperjars.com
Rather than just using the 3 "primary" colors in the logo please fell free to use complimentary colors as well as the monochromatic colors for each of the 3.
I will answer any questions you may have.
Company logo
Mild pepper
Hispanic designs
Happy pepper
Mean looking pepper
3 peppers
3 peppers #2
3 peppers #3
flaming peppers
habanero pepper

```html
<!DOCTYPE html>
<html lang="en">
<head>
<meta charset="utf-8">
<title>Abuela Rufina's Roasted Dip</title>
<link href="https://fonts.googleapis.com/css2?family=Arimo:ital,wght@0,400;0,700;1,400;1,700&family=Tinos:wght@700&display=swap" rel="stylesheet">
<style>
:root{
  --green:#0f7a2e;
  --yellow:#f5c400;
  --orange:#ee7a12;
  --red:#d8341a;
  --panel:#ffffff;
  --nav-bg:#fbe9dc;
  --nav-border:#e0503a;
  --ink:#111111;
  --muted:#888888;
  --field-border:#7a7a7a;
  --captcha:#d62020;
}
*{box-sizing:border-box;margin:0;padding:0}
html,body{width:1200px;height:751px;overflow:hidden}
body{position:relative;font-family:"Arimo",Arial,sans-serif;color:var(--ink);
  background:linear-gradient(180deg,var(--yellow) 0%,var(--orange) 45%,var(--red) 100%)}
.topbar{position:absolute;left:0;top:0;width:1200px;height:28px;background:var(--green)}
.topbar .contact{position:absolute;left:920px;top:7px;color:#fff;font-size:12px;font-weight:700}
.footer{position:absolute;left:0;top:715px;width:1200px;height:36px;background:var(--green);
  color:#fff;font-size:12px;font-weight:700;text-align:center;line-height:36px}
.brand{position:absolute;left:113px;top:0;width:283px;height:180px}
.brand svg{position:absolute;left:0;top:0}
.brand .name{position:absolute;left:36px;top:58px;width:220px;display:flex;align-items:center;gap:10px;
  font-size:21px;font-weight:700;color:var(--red);line-height:1.15}
.brand .name span.mark{flex:none;width:26px;height:26px;background:var(--green)}
.nav{position:absolute;left:137px;top:187px;width:247px;height:226px;background:var(--nav-bg);
  border:2px solid var(--nav-border)}
.nav ul{list-style:none;position:absolute;left:36px;top:26px}
.nav li{height:32.5px;display:flex;align-items:center;font-size:17px;font-weight:700}
.nav .pepper{width:22px;height:22px;margin-right:30px;border-radius:50% 50% 50% 10%;
  background:linear-gradient(135deg,#f3b400,#3aa030)}
.recipe{position:absolute;left:137px;top:425px;width:247px;height:288px;background:var(--panel)}
.recipe h2{height:31px;background:var(--green);color:#fff;font-size:17px;font-weight:700;padding:5px 0 0 14px}
.recipe .body{padding:9px 0 0 24px;font-size:14.5px;line-height:17.5px}
.recipe .body p{margin-bottom:17px}
.main{position:absolute;left:439px;top:67px;width:641px;height:648px;background:var(--panel)}
.main h1{position:absolute;left:52px;top:30px;font-family:"Tinos","Times New Roman",serif;font-size:23px;font-weight:700}
.testimonials{position:absolute;left:132px;top:68px;width:414px;font-size:14px;line-height:18px}
.testimonials blockquote{font-style:italic}
.testimonials cite{display:block;font-weight:700;font-style:italic;margin:12px 0 26px}
.pager{position:absolute;right:96px;top:317px;font-size:14px;font-weight:700}
.divider{position:absolute;left:120px;top:360px;width:414px;height:1px;background:#c8c8c8}
.field{position:absolute;border:1.5px solid var(--field-border);background:#fff;font-size:13px;color:var(--muted);padding:4px 7px}
.field.name{left:120px;top:391px;width:288px;height:30px}
.field.message{left:120px;top:432px;width:401px;height:94px}
.captcha{position:absolute;left:120px;top:540px;width:154px;height:41px;font-family:"Arimo",monospace;
  font-size:40px;font-weight:700;letter-spacing:4px;color:var(--captcha);line-height:41px}
.field.code{left:305px;top:545px;width:101px;height:26px}
.submit{position:absolute;left:449px;top:576px;width:60px;height:24px;background:var(--captcha);color:#fff;
  font-size:12px;text-align:center;line-height:24px;border:1px solid #a00}
</style>
</head>
<body>
<header class="topbar"><span class="contact">Contact info here</span></header>

<div class="brand">
  <svg width="283" height="180" viewBox="0 0 283 180" aria-hidden="true">
    <polygon points="0,0 283,0 270,180 13,180" fill="#fdf3e6"/>
  </svg>
  <div class="name"><span class="mark"></span>Abuela Rufina's Roasted Dip</div>
</div>

<nav class="nav">
  <ul>
    <li><span class="pepper" role="img" aria-label="small pepper icon"></span>About Us</li>
    <li><span class="pepper" role="img" aria-label="small pepper icon"></span>Testimonials</li>
    <li><span class="pepper" role="img" aria-label="small pepper icon"></span>Locations</li>
    <li><span class="pepper" role="img" aria-label="small pepper icon"></span>Recipes</li>
    <li><span class="pepper" role="img" aria-label="small pepper icon"></span>Buy Online</li>
    <li><span class="pepper" role="img" aria-label="small pepper icon"></span>Contact Us</li>
  </ul>
</nav>

<aside class="recipe">
  <h2>Recipe of the Day</h2>
  <div class="body">
    <p>Ingredients:</p>
    4 cups chopped vine-ripened tomatoes<br>
    2 cups dried black beans, cooked in salted water<br>
    &nbsp;until tender, cooled (about 2 cups)<br>
    1 cup small diced red onions<br>
    1 large fresh jalapeno,<br>
    &nbsp;seed and cut into small dice<br>
    1/2 cup loosely packed chopped fresh cilantro leaves<br>
    1 tablespoon chopped fresh parsley leaves
  </div>
</aside>

<main class="main">
  <h1>Testimonials</h1>
  <section class="testimonials">
    <blockquote>Quisque interdum velit non lectus mollis eu dignissim erat euismod. Donec pulvinar, ipsum non iaculis ornare, risus orci placerat elit, ac mattis sapien ligula dictum tellus. Vivamus gravida tempus erat, in eleifend orci volutpat et. Integer varius pulvinar quam, id tempor</blockquote>
    <cite>~ Anonymous</cite>
    <blockquote>Quisque interdum velit non lectus mollis eu dignissim erat euismod. Donec pulvinar, ipsum non iaculis ornare, risus orci placerat elit, ac mattis sapien ligula dictum tellus. Vivamus gravida tempus erat, in eleifend orci volutpat et. Integer varius pulvinar quam, id tempor</blockquote>
    <cite>~ Anonymous</cite>
  </section>
  <div class="pager">&lt;12345....10&gt;</div>
  <div class="divider"></div>
  <div class="field name">Name</div>
  <div class="field message">Message</div>
  <div class="captcha">mykn</div>
  <div class="field code"></div>
  <div class="submit">Submit</div>
</main>

<footer class="footer">Copy Right here</footer>
</body>
</html>
```